Ledge Crafts one page flyer

We need a standard A4 size flyer for a new company called Ledge Crafts. We are a construction material company and sell trims, crown mouldings, baseboards and panelings.
We would like to see the design with the following information:
1. Size: A4
2. Only one front page, no design need to display on back
3. Logo (Ledge Crafts, see the attached EPS file)
4. Slogan: We offer high quality products for competitive prices.
5. Content please see the PDF file
6. The production has 2 category, one called "Crown Moulding", the other is "Wainscoting", Crown Moulding has 5 productions, wainscoting has 2 production(Details see PDF file)
6. We temporary only can provide low resolution images for 7 productions, only the winner will be provided with High Resolution images.
Look and feel
Each slider illustrates characteristics of the customer's brand and the style your logo design should communicate.

```html
<!DOCTYPE html>
<html lang="en">
<head>
<meta charset="UTF-8">
<title>Ledge Crafts – Product Flyer</title>
<link href="https://fonts.googleapis.com/css2?family=Roboto:wght@300;400;500&display=swap" rel="stylesheet">
<style>
  :root {
    --page-bg: #3a3a3a;
    --paper: #ffffff;
    --ink-grey: #545e68;
    --accent-orange: #f15a29;
    --product-blue: #1f4fa6;
    --footer-blue: #2a50a8;
    --footer-deep: #253a86;
    --footer-label: #c9d3ec;
    --divider-grey: #b8bcc2;
    --tile-border: #ececec;
  }
  * { box-sizing: border-box; margin: 0; padding: 0; }
  html, body {
    width: 1200px; height: 1200px; overflow: hidden;
    background: var(--page-bg);
    font-family: "Roboto", Arial, sans-serif;
  }
  .flyer {
    position: absolute; left: 148px; top: 20px;
    width: 885px; height: 1137px;
    background: var(--paper);
    transform: scale(1.02); transform-origin: top left;
  }
  .brand {
    position: absolute; left: 118px; top: 66px;
    display: flex; align-items: center; gap: 26px;
  }
  .brand-square {
    width: 96px; height: 96px; background: var(--accent-orange);
  }
  .brand-name {
    font-weight: 500; font-size: 74px; letter-spacing: 7px;
    color: var(--ink-grey); line-height: 1;
  }
  .tagline {
    position: absolute; left: 270px; top: 156px;
    font-weight: 300; font-size: 27px; letter-spacing: 6.4px;
    color: var(--ink-grey);
  }
  .slogan-band {
    position: absolute; left: 0; top: 221px; width: 100%; height: 50px;
    background: var(--accent-orange); color: #fff;
    font-weight: 500; font-size: 22px; text-align: center; line-height: 50px;
  }
  .section-title {
    position: absolute; left: 68px;
    font-weight: 300; font-size: 38px; color: var(--ink-grey);
  }
  .section-rule {
    position: absolute; left: 70px; width: 390px; height: 1px;
    background: linear-gradient(90deg, #2a3e8c, rgba(42,62,140,0));
  }
  .product { position: absolute; display: flex; gap: 34px; }
  .product-tile {
    width: 107px; height: 107px; border: 1px solid var(--tile-border);
    border-radius: 6px; background: #fafafa;
    box-shadow: 0 1px 3px rgba(0,0,0,0.06);
  }
  .product-tile.profile {
    background: linear-gradient(135deg, #fdfdfd 30%, #9a9a9a 48%, #1a1a1a 52%, #f2f2f2 62%, #fafafa);
  }
  .product-text {
    padding-top: 19px; font-size: 18px; line-height: 22px;
    color: var(--product-blue); font-weight: 400;
  }
  .product-size { color: #333; }
  .footer-divider {
    position: absolute; left: 0; top: 1002px; width: 100%; height: 8px;
    background: var(--divider-grey);
  }
  .footer {
    position: absolute; left: 0; top: 1010px; width: 100%; height: 127px;
    background: var(--footer-blue); color: #fff;
  }
  .footer-hours {
    position: absolute; left: 0; top: 0; width: 292px; height: 100%;
    background: var(--footer-deep); padding: 20px 0 0 60px;
  }
  .footer-label { color: var(--footer-label); font-size: 18px; margin-bottom: 6px; }
  .hours { font-size: 16px; line-height: 19px; display: grid; grid-template-columns: 85px auto; }
  .contact { position: absolute; left: 320px; top: 20px; }
  .contact-body { display: flex; gap: 12px; }
  .office { font-size: 16px; line-height: 19px; }
  .office small { font-size: 10.5px; line-height: 13px; display: inline; }
  .contact-split { width: 1px; background: rgba(255,255,255,0.5); margin-top: 8px; height: 42px; }
  .direct { font-size: 16px; line-height: 19px; padding-top: 12px; }
  .warehouse { position: absolute; left: 690px; top: 20px; }
  .warehouse-body { font-size: 11px; line-height: 13.5px; font-weight: 500; }
</style>
</head>
<body>
<main class="flyer">
  <header>
    <div class="brand">
      <div class="brand-square"></div>
      <div class="brand-name">LEDGE CRAFTS</div>
    </div>
    <p class="tagline">FOR ALL TYPES OF PROJECTS</p>
  </header>

  <div class="slogan-band">WE OFFER HIGH QUALITY PRODUCTS FOR COMPETITIVE PRICES.</div>

  <h2 class="section-title" style="top:300px">CROWN MOULDING</h2>
  <div class="section-rule" style="top:347px"></div>

  <div class="product" style="left:66px; top:368px">
    <div class="product-tile profile" role="img" aria-label="Tuscany 9 crown moulding profile"></div>
    <div class="product-text">TUSCANY 9<br>CROWN MOULDING<br><span class="product-size">8 7/16"X3/4"</span></div>
  </div>
  <div class="product" style="left:419px; top:368px">
    <div class="product-tile profile" role="img" aria-label="Tuscany 7 crown moulding profile"></div>
    <div class="product-text" style="margin-left:6px">TUSCANY 7<br>CROWN MOULDING<br><span class="product-size">6 1/2"X3/4"</span></div>
  </div>
  <div class="product" style="left:66px; top:500px">
    <div class="product-tile profile" role="img" aria-label="Tuscany 8 crown moulding profile"></div>
    <div class="product-text">TUSCANY 8<br>CROWN MOULDING<br><span class="product-size">7 3/4"X3/4"</span></div>
  </div>
  <div class="product" style="left:419px; top:500px">
    <div class="product-tile profile" role="img" aria-label="Milan 8 crown moulding profile"></div>
    <div class="product-text" style="margin-left:6px">MILAN 8<br>CROWN MOULDING<br><span class="product-size">7 3/4"X3/4"</span></div>
  </div>
  <div class="product" style="left:66px; top:636px">
    <div class="product-tile profile" role="img" aria-label="Milan 6 crown moulding profile"></div>
    <div class="product-text">MILAN 6<br>CROWN MOULDING<br><span class="product-size">6 1/4"X3/4"</span></div>
  </div>

  <h2 class="section-title" style="top:786px">WAINSCOTING</h2>
  <div class="section-rule" style="top:833px"></div>

  <div class="product" style="left:65px; top:858px">
    <div class="product-tile" role="img" aria-label="Colonial chair rail profile"></div>
    <div class="product-text">COLONIAL<br>CHAIR RAIL<br><span class="product-size">3 1/4"X1"</span></div>
  </div>
  <div class="product" style="left:419px; top:858px">
    <div class="product-tile" role="img" aria-label="Colonial panel mould profile"></div>
    <div class="product-text">COLONIAL<br>PANEL MOULD<br><span class="product-size">1 3/4"X5/8"</span></div>
  </div>

  <div class="footer-divider"></div>
  <footer class="footer">
    <div class="footer-hours">
      <div class="footer-label">OFFICE HOURS</div>
      <div class="hours">
        <span>Mon – Fri</span><span>: 7:00am – 6.00pm</span>
        <span>Saturdays</span><span>: 8:00am – 4.00pm</span>
        <span>Sundays</span><span>: Closed</span>
      </div>
    </div>
    <div class="contact">
      <div class="footer-label">CONTACT INFORMATION</div>
      <div class="contact-body">
        <div class="office">Ledge Crafts<br>Office: <small>417 Harbour Ave, unit 2<br>Brookfield, Ontario L5K 1R8</small></div>
        <div class="contact-split"></div>
        <div class="direct">905-555-0142<br>info@ledgecrafts.ca</div>
      </div>
    </div>
    <div class="warehouse">
      <div class="footer-label">WAREHOUSE:</div>
      <div class="warehouse-body">88 Millstone Rd<br>Eastvale, ON M4T 3B6<br>By Appointment Only</div>
    </div>
  </footer>
</main>
</body>
</html>
```